Foot and ankle surgeon requires a website design

I need a website where prospective and established patients can obtain information and then direct them to making appointments. My practice is a highly professional surgical practice specialising in surgery to the foot and ankle. My title is Mr Colin Dravers, Podiatric Foot & Ankle Surgeon. My qualifications are: BSc MSc FACPS
The practice website will require information on: Locations, phone numbers to make appointments, general background on podiatric surgery,
I would like to include information on: my hospital appointments, surgical fellowships held, training programs undertaken, association memberships, publications written, links to useful websites
A page dedicated to common foot conditions would be useful and also a page with referral information including an online registration section that will be sent direct to the receptionist.
Examples of similar websites include:
http://www.jorbellianfeet.com.au/
http://www.quandrilfootsurgeon.com.au/
I will provide files on logo, self photos and my personal training history etc.
Also if there is going to be a background theme I personally am associated with surfing and beach activities, it would be great if this was able to be reflected in the design.
Thank you.

```html
<!DOCTYPE html>
<html lang="en">
<head>
<meta charset="utf-8">
<title>Mr Colin Dravers – Podiatric Foot &amp; Ankle Surgeon</title>
<link rel="stylesheet" href="https://fonts.googleapis.com/css2?family=Rajdhani:wght@300;400;500;600;700&family=Open+Sans:wght@400;600&display=swap">
<style>
  :root {
    --ocean: #0aa3e0;
    --ocean-deep: #0a62c4;
    --ocean-mid: #0b86d6;
    --ink: #111417;
    --paper: #ffffff;
    --rule: #e3e6e8;
    --accent: #29a8e0;
    --muted: #555a5e;
  }
  * { box-sizing: border-box; margin: 0; padding: 0; }
  html, body { width: 1200px; height: 606px; overflow: hidden; background: var(--paper); }
  body { position: relative; font-family: "Rajdhani", "Arial Narrow", sans-serif; color: var(--ink); }

  .hero {
    position: absolute; left: 0; top: 0; width: 1200px; height: 390px;
    background:
      radial-gradient(ellipse 520px 200px at 180px 60px, rgba(10, 70, 170, 0.55), transparent 70%),
      linear-gradient(180deg, var(--ocean-mid) 0%, var(--ocean) 45%, var(--ocean-deep) 100%);
  }

  .brand {
    position: absolute; left: 254px; top: 32px;
    display: flex; align-items: center; gap: 8px;
    color: var(--paper); font-weight: 600; font-size: 16px; letter-spacing: 0.2px;
    white-space: nowrap;
  }
  .brand-dot { width: 10px; height: 10px; border-radius: 50%; background: var(--paper); }

  .menu-button {
    position: absolute; left: 875px; top: 29px; width: 72px; height: 29px;
    border: 1px solid var(--paper); color: var(--paper);
    font-size: 13px; font-weight: 500; padding: 10px 0 0 2px; line-height: 1;
  }
  .menu-button svg { position: absolute; right: 5px; top: 15px; }

  .hero-title {
    position: absolute; left: 0; width: 1200px; top: 190px; text-align: center;
    color: var(--paper); font-size: 36px; letter-spacing: 1px; line-height: 1;
    white-space: nowrap;
  }
  .hero-title .light { font-weight: 300; }
  .hero-title .bold { font-weight: 700; }
  .hero-arrows { position: absolute; left: 572px; top: 243px; }

  .info-card { position: absolute; width: 130px; border: 2px solid var(--ink); background: var(--paper); }
  .info-card.split { border: none; background: none; }
  .card-head {
    position: relative; height: 25px; padding: 6px 0 0 4px;
    font-size: 13px; font-weight: 700; text-transform: uppercase; line-height: 1;
    white-space: nowrap;
  }
  .card-head small { font-size: 9px; font-weight: 600; }
  .card-head svg { position: absolute; right: 4px; top: 5px; }
  .split .card-head { border: 2px solid var(--paper); border-bottom: none; color: var(--paper); }
  .split .card-body {
    border: 2px solid var(--ink); background: var(--paper); height: 29px;
    padding: 6px 0 0 3px; font-size: 15px; font-weight: 700; line-height: 1;
    white-space: nowrap; overflow: hidden;
  }
  .split .card-body.address { font-size: 14px; font-variant: small-caps; letter-spacing: 0; padding-top: 5px; }
  .phone-prefix { font-weight: 400; color: var(--muted); }

  .card-phone { left: 281px; top: 365px; }
  .card-clinic { left: 620px; top: 365px; }
  .card-hours { left: 451px; top: 424px; height: 54px; }
  .card-register { left: 790px; top: 400px; height: 53px; border-color: var(--accent); }

  .card-hours .card-head, .card-register .card-head { height: 22px; padding-top: 5px; }
  .small-line { font-size: 9px; font-weight: 700; padding-left: 4px; line-height: 1.1; text-transform: uppercase; white-space: nowrap; }
  .card-register .small-line { margin-top: 3px; }
  .highlight { color: var(--accent); font-size: 13px; font-weight: 700; padding-left: 4px; line-height: 1; white-space: nowrap; }
  .highlight small { font-size: 9px; }
  .card-register .highlight { font-size: 14px; text-transform: uppercase; }

  .footer-rule { position: absolute; left: 0; top: 518px; width: 1200px; height: 1px; background: var(--rule); }
  .copyright {
    position: absolute; left: 778px; top: 534px; padding-left: 5px;
    border-left: 2px solid var(--ink); white-space: nowrap;
    font-family: "Open Sans", Arial, sans-serif; font-size: 7px; font-weight: 600; line-height: 9px;
  }
</style>
</head>
<body>
  <header class="hero" role="img" aria-label="Photograph of a surfer holding a longboard on a misty beach, toned blue">
  </header>

  <div class="brand"><span class="brand-dot"></span>Mr Colin Dravers</div>

  <nav class="menu-button">MENU
    <svg width="11" height="9" viewBox="0 0 11 9" fill="#fff"><rect width="11" height="2"/><rect y="3.5" width="11" height="2"/><rect y="7" width="11" height="2"/></svg>
  </nav>

  <h1 class="hero-title"><span class="light">FOOT</span> <span class="bold">KNOWLEDGE</span></h1>
  <svg class="hero-arrows" width="54" height="12" viewBox="0 0 54 12" fill="none" stroke="#fff" stroke-width="1.3">
    <path d="M6 1 L1 6 L6 11"/><path d="M9 6 H52"/><path d="M47 1 L52 6 L47 11"/>
  </svg>

  <section class="info-card split card-phone">
    <div class="card-head">Phone <small>number</small>
      <svg width="10" height="12" viewBox="0 0 10 12" fill="#fff"><path d="M2 0 L4 3 L3 4.5 C4 7 5 8.5 6.5 9.5 L8 8.5 L10 11 L8.5 12 C4 11 1 6 0.5 1.5 Z"/></svg>
    </div>
    <div class="card-body"><span class="phone-prefix">(05)</span> 3862 7041</div>
  </section>

  <section class="info-card split card-clinic">
    <div class="card-head">Clinic <small>address</small>
      <svg width="10" height="13" viewBox="0 0 10 13"><path d="M5 13 C5 13 0 7 0 5 A5 5 0 0 1 10 5 C10 7 5 13 5 13 Z" fill="#fff"/><circle cx="5" cy="5" r="2" fill="#1a8ad6"/></svg>
    </div>
    <div class="card-body address">47 Tarrin Street, Perth</div>
  </section>

  <section class="info-card card-hours">
    <div class="card-head">Office <small>hour</small>
      <svg width="13" height="13" viewBox="0 0 13 13" fill="none" stroke="#29a8e0" stroke-width="1.4"><circle cx="6.5" cy="6.5" r="5.6"/><path d="M6.5 3 V6.8 H9"/></svg>
    </div>
    <p class="small-line">Monday - Friday</p>
    <p class="highlight">9:00<small>AM</small> - 5:00<small>PM</small></p>
  </section>

  <section class="info-card card-register">
    <div class="card-head">Registration
      <svg width="12" height="13" viewBox="0 0 12 13" fill="#29a8e0"><circle cx="6" cy="3.5" r="3.3"/><path d="M0 13 C0 8.5 2.5 7 6 7 C9.5 7 12 8.5 12 13 Z"/></svg>
    </div>
    <p class="small-line">Online</p>
    <p class="highlight">Registration</p>
  </section>

  <div class="footer-rule"></div>
  <footer class="copyright">Mr Colin Dravers, All rights reserved 2014.</footer>
</body>
</html>
```